Veltrano Energy Business Card Design

website: www.veltranoenergy.example
Project: Business Card Design for Veltrano Energy
Name: Dorian Kettle
Title: Founder / Operations Strategist
Visual Identity & Logo:
Logo File: VEL-Logo-FullGradient-Final.png (Attached).
Color Palette: The brand relies on a distinctive Cyan (Blue) to Lime Green gradient.
Background Preference: We want a Dark Mode aesthetic (Deep Matte Black, Charcoal, or Dark Slate) to make the neon gradient of the logo pop. This feels more "tech/industrial" than a standard white card.
Design Aesthetic (The "Ops" Vibe):
Concept: "Grid & Infrastructure." We are a solar rental company, focusing on logistics and access.
Typography: White, bold sans-serif text for contact info. High contrast against the dark background.
Accents: Use the Cyan or Lime Green from the logo for thin divider lines or edge painting.
Avoid: No orange/gold (clashes with logo). No cartoon leaves.
Layout Requirements:
Front: Large, centered logo. Maybe a subtle UV gloss spot varnish over the logo icon.
Back: Name, Title, Contact Info.
Texture: Matte finish cardstock with gloss elements.
sample mock up of information on card: https://brivomarkco-my.filehost.example/:i:/g/personal/dorian_kettle_veltranoenergy_example/AbCdEfGhIjKlMnOpQrStUvWxYz012345678?e=Xy12Ab
Logo: https://brivomarkco.filehost.example/:i:/s/VeltranoEnergy/ZyXwVuTsRqPoNmLkJiHgFeDcBa9876543210?e=Pq34Cd

```html
<!DOCTYPE html>
<html lang="en">
<head>
<meta charset="utf-8">
<title>Veltrano Energy – Business Card</title>
<link href="https://fonts.googleapis.com/css2?family=Open+Sans:ital,wght@1,400&family=Poppins:wght@400;500;600;700&display=swap" rel="stylesheet">
<style>
  :root {
    --bg: #3a3a3a;
    --card: #1e1e1e;
    --cyan: #12a6df;
    --teal: #1ec9b8;
    --lime: #9bdb26;
    --ring: #6fcf3a;
    --white: #ffffff;
    --soft: #d8d8d8;
    --ink: #111111;
  }
  * { box-sizing: border-box; margin: 0; padding: 0; }
  html, body { width: 1200px; height: 875px; overflow: hidden; }
  body {
    background: var(--bg);
    font-family: "Poppins", Arial, sans-serif;
    color: var(--white);
    position: relative;
  }
  .card {
    position: absolute;
    left: 240px;
    width: 720px;
    height: 410px;
    background: var(--card);
    border-radius: 22px;
    overflow: hidden;
    box-shadow: 0 10px 30px rgba(0,0,0,.45);
  }
  .card--front { top: 22px; }
  .card--back  { top: 446px; }

  /* Wordmark */
  .wordmark { position: absolute; display: flex; align-items: center; }
  .wordmark__mark { background: var(--cyan); border-radius: 6px; flex: none; }
  .wordmark__name { color: var(--teal); font-weight: 500; letter-spacing: .5px; white-space: nowrap; }

  .card--front .wordmark { left: 92px; top: 70px; gap: 22px; }
  .card--front .wordmark__mark { width: 70px; height: 70px; }
  .card--front .wordmark__name { font-size: 54px; line-height: 1; }
  .front-tagline {
    position: absolute; left: 186px; top: 152px;
    font-family: "Open Sans", Arial, sans-serif; font-style: italic;
    font-size: 19px; color: var(--white);
  }

  .features {
    position: absolute; left: 60px; right: 60px; top: 232px;
    display: flex; justify-content: space-between;
  }
  .feature { width: 140px; text-align: center; }
  .feature__icon {
    width: 60px; height: 60px; margin: 0 auto 10px;
    border-radius: 50%; border: 2px solid var(--ring);
    padding: 4px; background-clip: content-box;
    background-color: transparent;
  }
  .feature__icon span {
    display: block; width: 100%; height: 100%; border-radius: 50%;
    background: radial-gradient(circle at 40% 40%, #ffffff 0 30%, #bfe4f6 55%, #4aa8e0 100%);
  }
  .feature__label { font-size: 12.5px; line-height: 1.35; color: var(--white); }

  /* Back */
  .card--back .wordmark { right: 46px; top: 40px; gap: 12px; }
  .card--back .wordmark__mark { width: 34px; height: 34px; border-radius: 4px; }
  .card--back .wordmark__name { font-size: 28px; line-height: 1; }
  .back-tagline {
    position: absolute; right: 46px; top: 82px;
    font-family: "Open Sans", Arial, sans-serif; font-style: italic;
    font-size: 9.5px; color: var(--white);
  }

  .person { position: absolute; left: 44px; top: 120px; }
  .person__name {
    font-size: 30px; font-weight: 700; letter-spacing: .5px; text-transform: uppercase;
    background: linear-gradient(90deg, var(--cyan), var(--lime));
    -webkit-background-clip: text; background-clip: text; color: transparent;
  }
  .person__title { font-size: 16px; font-weight: 500; margin-top: 2px; }

  .contact { position: absolute; left: 150px; top: 208px; font-size: 15.5px; font-weight: 500; line-height: 1.35; }
  .contact__address { margin-bottom: 8px; }
  .contact__row { display: flex; align-items: center; gap: 8px; }
  .contact__row svg { width: 14px; height: 14px; flex: none; }

  .offices { position: absolute; right: 70px; top: 170px; text-align: left; }
  .offices__label { font-size: 15px; font-weight: 500; margin-bottom: 6px; }
  .offices__flags { display: flex; gap: 4px; }
  .offices__flags span {
    width: 34px; height: 34px; border-radius: 50%; border: 2px solid var(--soft);
  }
  .flag-a { background: linear-gradient(135deg, #2b3f8c 0 45%, #c9323c 45% 70%, #f2f2f2 70%); }
  .flag-b { background: linear-gradient(90deg, #d52b1e 0 28%, #f4f4f4 28% 72%, #d52b1e 72%); }
  .flag-c { background: linear-gradient(135deg, #1f3a8a 0 40%, #f1f1f1 40% 55%, #c8102e 55% 65%, #1f3a8a 65%); }

  .band { position: absolute; left: 0; bottom: 0; width: 720px; height: 90px; }
  .band__text {
    position: absolute; left: 60px; bottom: 14px;
    font-size: 15px; font-weight: 500; color: var(--ink);
  }
</style>
</head>
<body>

<section class="card card--front" aria-label="Card front">
  <div class="wordmark">
    <span class="wordmark__mark"></span>
    <span class="wordmark__name">Veltrano Energy</span>
  </div>
  <p class="front-tagline">Rent Solar. Generate Power. Save Smarter</p>

  <ul class="features" style="list-style:none">
    <li class="feature">
      <div class="feature__icon"><span role="img" aria-label="Piggy bank illustration"></span></div>
      <p class="feature__label">No Money Out<br>of Pocket</p>
    </li>
    <li class="feature">
      <div class="feature__icon"><span role="img" aria-label="Rising energy illustration"></span></div>
      <p class="feature__label">Guaranteed Energy<br>Production</p>
    </li>
    <li class="feature">
      <div class="feature__icon"><span role="img" aria-label="Rental agreement document illustration"></span></div>
      <p class="feature__label">Simple Rental<br>Agreement</p>
    </li>
    <li class="feature">
      <div class="feature__icon"><span role="img" aria-label="Globe with leaf illustration"></span></div>
      <p class="feature__label">Sustainable<br>Impact</p>
    </li>
  </ul>
</section>

<section class="card card--back" aria-label="Card back">
  <div class="wordmark">
    <span class="wordmark__mark"></span>
    <span class="wordmark__name">Veltrano Energy</span>
  </div>
  <p class="back-tagline">Rent Solar. Generate Power. Save Smarter</p>

  <div class="person">
    <h1 class="person__name">Dorian Kettle</h1>
    <p class="person__title">Founder / Operations Strategist</p>
  </div>

  <div class="contact">
    <p class="contact__address">Veltrano Energy<br>4120 Marlow Crest Drive<br>Brennick, FL 30917</p>
    <p class="contact__row">
      <svg viewBox="0 0 16 16" aria-hidden="true"><path d="M3 1.5l3 3-1.5 2a9 9 0 0 0 5 5l2-1.5 3 3-2 2C7 15 1 9 1 3.5z" fill="#1ec9b8"/></svg>
      555.014.2286
    </p>
    <p class="contact__row">
      <svg viewBox="0 0 16 16" aria-hidden="true"><circle cx="8" cy="8" r="7" fill="#12a6df"/><path d="M1 8h14M8 1c3 3 3 11 0 14M8 1c-3 3-3 11 0 14" stroke="#9bdb26" stroke-width="1.2" fill="none"/></svg>
      www.veltranoenergy.example
    </p>
  </div>

  <div class="offices">
    <p class="offices__label">Office</p>
    <div class="offices__flags">
      <span class="flag-a" role="img" aria-label="United States flag"></span>
      <span class="flag-b" role="img" aria-label="Canada flag"></span>
      <span class="flag-c" role="img" aria-label="United Kingdom flag"></span>
    </div>
  </div>

  <svg class="band" viewBox="0 0 720 90" aria-hidden="true">
    <defs>
      <linearGradient id="bandMain" x1="0" x2="1" y1="0" y2="0">
        <stop offset="0" stop-color="#12a6df"/>
        <stop offset="0.55" stop-color="#3fcf8a"/>
        <stop offset="1" stop-color="#9bdb26"/>
      </linearGradient>
      <linearGradient id="bandEnd" x1="0" x2="1" y1="0" y2="0">
        <stop offset="0" stop-color="#12a6df"/>
        <stop offset="0.5" stop-color="#1ec9b8"/>
        <stop offset="1" stop-color="#9bdb26"/>
      </linearGradient>
    </defs>
    <path d="M0 56 H500 C512 56 514 48 520 40 L520 90 H0 Z" fill="url(#bandMain)"/>
    <path d="M532 90 C540 70 538 52 552 40 L566 40 C552 52 556 72 548 90 Z" fill="#9bdb26"/>
    <path d="M562 90 C570 70 568 52 582 40 H720 V90 Z" fill="url(#bandEnd)"/>
  </svg>
  <p class="band__text">No debt, no liens, no maintenance, just savings.</p>
</section>

</body>
</html>
```